Dermatology Office Business Card Update

Updating some information on the current business card. Do not adjust font type. Need both rounded rectangle and rounded square card files. In addition, must have separate file for both rectangle and square cards for gold foil printing.1. Update phone number with: 555-318-27602. Remove email address3. Add this website to be listed under quillbrookdermatology.example:jilluxe.com4. Under updated phone number, add the flickvue logo in color and then a space and the following text: @dermjill5. Gold foil should be inclusive of the outline of the butterfly wings on the front. Also should put a small hyphen that is also gold foil under the cursive Nora Belcastro, MD and before the block lettering begins.Back of card remains the samePlease feel free to contact me with any questions!

Target Market(s)

Patients

Contact Information for Business Card

Just needs some updates along with files for gold foil printing

Requirements
Must have
• Updating some information on the current business card. Do not adjust font type. Need both rounded rectangle and rounded square card files. In addition, must have separate file for both rectangle and square cards for gold foil printing.
• 1. Update phone number with: 555-318-2760
• 2. Remove email address
• 3. Add this website to be listed under quillbrookdermatology.example:
• norvatek.example
• 4. Under updated phone number, add the flickvue logo in color and then a space and the following text: @docnorabel
• 5. Gold foil should be inclusive of the outline of the butterfly wings on the front. Also should put a small hyphen that is also gold foil under the cursive Nora Belcastro, MD and before the block lettering begins.
• Back of card remains the same
• Please feel free to contact me with any questions!

```html
<!DOCTYPE html>
<html lang="en">
<head>
<meta charset="utf-8">
<title>Quillbrook Dermatology – Business Card</title>
<link rel="stylesheet" href="https://fonts.googleapis.com/css2?family=Raleway:wght@400;500&display=swap">
<style>
  :root {
    --backdrop: #a27274;
    --card-white: #ffffff;
    --navy: #2b3a5c;
    --rose: #c98f93;
    --mauve: #8e6470;
    --plum: #6c5672;
    --gold: #c9a54a;
  }
  * { box-sizing: border-box; margin: 0; padding: 0; }
  html, body {
    width: 1200px; height: 807px; overflow: hidden;
    background: var(--backdrop);
    font-family: "Raleway", sans-serif;
  }
  .stage { position: relative; width: 1200px; height: 807px; }
  .card {
    position: absolute; top: 255px;
    width: 520px; height: 297px;
    border-radius: 22px; overflow: hidden;
    box-shadow: 0 4px 14px rgba(40, 30, 50, 0.35);
  }

  /* Front */
  .card-front { left: 50px; background: var(--card-white); }
  .brand-lockup {
    position: absolute; left: 44px; top: 50px; width: 250px;
    display: flex; align-items: center; gap: 12px;
  }
  .brand-mark {
    width: 34px; height: 34px; border-radius: 50%;
    background: var(--rose); flex: none;
  }
  .brand-name {
    font-weight: 500; font-size: 16px; letter-spacing: 3px;
    line-height: 1.4; text-transform: uppercase; color: var(--navy);
  }
  .foil-dash {
    position: absolute; left: 90px; top: 120px;
    width: 22px; height: 2px; background: var(--gold);
  }
  .doctor-name {
    position: absolute; left: 44px; bottom: 58px;
    font-weight: 500; font-size: 22px; letter-spacing: 0.5px;
    color: var(--navy); text-transform: uppercase;
  }
  .doctor-name .credential { color: var(--rose); }
  .contact-list {
    position: absolute; left: 262px; top: 44px;
    list-style: none; display: flex; flex-direction: column; gap: 7px;
  }
  .contact-item {
    display: flex; align-items: center; gap: 8px;
    font-size: 14px; color: var(--navy); white-space: nowrap;
  }
  .contact-icon { width: 13px; height: 13px; flex: none; }
  .social-square {
    width: 12px; height: 12px; background: var(--gold); flex: none; margin: 0 1px;
  }
  .front-band {
    position: absolute; left: 0; right: 0; bottom: 0; height: 34px;
    background: linear-gradient(90deg, var(--navy) 0%, var(--plum) 35%, var(--mauve) 70%, var(--rose) 100%);
    border-top: 3px solid var(--gold);
  }

  /* Back */
  .card-back { left: 630px; }
  .back-texture {
    position: absolute; inset: 0;
    background: linear-gradient(200deg, #9a6b74 0%, #8b6470 45%, #6d5c78 80%, #3f4b6c 100%);
  }
  .back-lockup {
    position: absolute; inset: 0;
    display: flex; flex-direction: column; align-items: center; justify-content: center; gap: 18px;
  }
  .back-brand {
    font-weight: 500; font-size: 22px; letter-spacing: 4px;
    text-transform: uppercase; color: var(--card-white);
  }
  .tagline {
    font-weight: 400; font-size: 12px; letter-spacing: 4px;
    text-transform: uppercase; color: var(--card-white);
  }
</style>
</head>
<body>
<main class="stage">

  <section class="card card-front" aria-label="Business card front">
    <div class="brand-lockup">
      <span class="brand-mark"></span>
      <span class="brand-name">Quillbrook<br>Dermatology</span>
    </div>
    <span class="foil-dash"></span>

    <ul class="contact-list">
      <li class="contact-item">
        <svg class="contact-icon" viewBox="0 0 16 16"><path fill="var(--gold)" d="M3 1h3l1.5 4-2 1.3a9 9 0 0 0 4.2 4.2L11 8.5l4 1.5v3a2 2 0 0 1-2 2A12 12 0 0 1 1 3a2 2 0 0 1 2-2z"/></svg>
        555-318-2760
      </li>
      <li class="contact-item">
        <span class="social-square"></span>
        @docnorabel
      </li>
      <li class="contact-item">
        <svg class="contact-icon" viewBox="0 0 16 16"><g fill="none" stroke="var(--gold)" stroke-width="1.4"><circle cx="8" cy="8" r="6.5"/><ellipse cx="8" cy="8" rx="3" ry="6.5"/><path d="M1.5 8h13"/></g></svg>
        quillbrookdermatology.example
      </li>
      <li class="contact-item">
        <span class="contact-icon"></span>
        norvatek.example
      </li>
    </ul>

    <p class="doctor-name">Nora Belcastro, <span class="credential">MD</span></p>
    <div class="front-band"></div>
  </section>

  <section class="card card-back" aria-label="Business card back">
    <div class="back-texture" role="img" aria-label="Rose to navy watercolour wash texture"></div>
    <div class="back-lockup">
      <span class="back-brand">Quillbrook</span>
      <span class="tagline">Renewing Skin</span>
    </div>
  </section>

</main>
</body>
</html>
```